New Business Card

Would like a shiny card with Metallic logo raised on th front. Address 418 Kestwick Lane, Toronto Ontario M4T2B8, phone 416 555 0382, email kmvc@lorentel.ca and web www.kmvc.ca on the back in right and left lower corners balanced. Top of back should say Personalized Care for Pet's and their People centered. Leaving space on the back to write. Horizontal placement

```html
<!DOCTYPE html>
<html lang="en">
<head>
<meta charset="utf-8">
<title>Kestwick Meadow Vet Clinic – Business Card</title>
<link rel="stylesheet" href="https://fonts.googleapis.com/css2?family=Open+Sans:wght@400;600&family=Roboto+Condensed:wght@700&display=swap">
<style>
  :root {
    --backdrop: #ececec;
    --card-dark: #1f1f1f;
    --card-light: #ffffff;
    --ink: #1a1a1a;
    --ink-soft: #2b2b2b;
    --silver: #c4c4c4;
  }
  * { margin: 0; padding: 0; box-sizing: border-box; }
  html, body {
    width: 1200px; height: 1000px; overflow: hidden;
    background: var(--backdrop);
    font-family: "Open Sans", Arial, sans-serif;
  }
  .canvas { position: relative; width: 1200px; height: 1000px; }

  .card {
    position: absolute; left: 266px; width: 666px; height: 397px;
    border-radius: 24px;
    box-shadow: 0 4px 14px rgba(0,0,0,0.18);
  }
  .card--front { top: 75px; background: var(--card-dark); }
  .card--back { top: 533px; background: var(--card-light); }

  .brand {
    position: absolute; top: 96px; left: 0; right: 0;
    display: flex; flex-direction: column; align-items: center;
  }
  .brand__dot {
    width: 124px; height: 124px; border-radius: 50%;
    background: var(--silver); margin-bottom: 26px;
  }
  .brand__name {
    color: var(--silver); font-weight: 600;
    font-size: 34px; letter-spacing: 1px; text-transform: uppercase;
    text-align: center; line-height: 1.1;
  }
  .brand__sub {
    color: var(--silver); font-weight: 600;
    font-size: 17px; letter-spacing: 1px; text-transform: uppercase;
    margin-top: 6px;
  }

  .tagline {
    position: absolute; top: 26px; left: 0; right: 0;
    text-align: center; color: var(--ink);
    font-size: 18px; font-weight: 400;
  }
  .contact-block {
    position: absolute; top: 168px; left: 0; right: 0;
    display: flex; justify-content: center; align-items: center;
  }
  .person { text-align: right; padding-right: 20px; }
  .person__name {
    font-family: "Roboto Condensed", "Arial Narrow", sans-serif;
    font-weight: 700; font-size: 29px; color: var(--ink);
    line-height: 1.05; text-transform: uppercase;
  }
  .person__role { font-size: 15px; color: var(--ink-soft); margin-top: 4px; }
  .divider { width: 2px; height: 56px; background: var(--ink); }
  .details { list-style: none; padding-left: 20px; }
  .details li {
    display: flex; align-items: center; gap: 7px;
    font-size: 15px; color: var(--ink-soft); line-height: 20.5px;
  }
  .details svg { width: 14px; height: 14px; fill: var(--ink); }

  .address {
    position: absolute; bottom: 28px; left: 0; right: 0;
    text-align: center; font-size: 16px; color: var(--ink);
  }
</style>
</head>
<body>
<div class="canvas">
  <section class="card card--front">
    <div class="brand">
      <div class="brand__dot"></div>
      <div class="brand__name">Kestwick Meadow</div>
      <div class="brand__sub">Vet Clinic</div>
    </div>
  </section>

  <section class="card card--back">
    <p class="tagline">Personalized Care for Pet's and their People</p>
    <div class="contact-block">
      <div class="person">
        <div class="person__name">Nora Halvik</div>
        <div class="person__role">Managing Partner</div>
      </div>
      <div class="divider"></div>
      <ul class="details">
        <li>
          <svg viewBox="0 0 16 16" aria-hidden="true"><path d="M2 6c0-2 2-3 6-3s6 1 6 3v1h-3V5.5H5V7H2z M4 8h8l1.5 5h-11z"/></svg>
          416 555 0382
        </li>
        <li>
          <svg viewBox="0 0 16 16" aria-hidden="true"><path d="M1 3h14v1.5L8 9 1 4.5z M1 6l7 4.5L15 6v7H1z"/></svg>
          kmvc@lorentel.ca
        </li>
        <li>
          <svg viewBox="0 0 16 16" aria-hidden="true"><path d="M8 1a7 7 0 1 0 0 14A7 7 0 0 0 8 1zm0 2a5 5 0 0 1 0 10A5 5 0 0 1 8 3z"/><path d="M5 5h3l1 2-2 1 1 3H6L5 8z"/></svg>
          www.kmvc.ca
        </li>
      </ul>
    </div>
    <p class="address">418 Kestwick Lane, Toronto Ontario M4T2B8</p>
  </section>
</div>
</body>
</html>
```